Classy, Elegant, Simple Business Card Design

Looking to have a classy, simple, and elegant design. Want a top notch designed business card. I really like the look of the new brivo credit card. I also like the design I attached. I am trying to reach 21-29 year old females for booking us for there wedding or event. We offer Disc Jockey Service, Photo Booth Rentals, and Uplighting .

Target Market(s)

21-28 year old females

Contact Information for Business Card

Has to have logo, website, email, and phone number

Font styles to use
Other font styles liked:
• open to font choice, modern, clean
Designer to choose
33a6d7
0791cd
0555a3
ffffff

Requirements
Must have
• Has to have logo, website, email, and phone number
Nice to have
• I really like the design of the new brivo credit card. I also included my logo and some designs I like
Should not have
• clutter or too much info

```html
<!DOCTYPE html>
<html lang="en">
<head>
<meta charset="utf-8">
<title>Tidewell Events – Business Card</title>
<link rel="stylesheet" href="https://fonts.googleapis.com/css2?family=Quicksand:wght@500;600&display=swap">
<style>
  :root {
    --sky: #33a6d7;
    --azure: #0791cd;
    --deep: #0555a3;
    --paper: #ffffff;
    --backdrop: #e9ecef;
  }
  html, body {
    margin: 0;
    width: 1200px;
    height: 801px;
    overflow: hidden;
    background: var(--backdrop);
  }
  .card {
    position: absolute;
    left: 150px;
    top: 124px;
    width: 900px;
    height: 552px;
    background: var(--paper);
    box-shadow: 0 6px 24px rgba(0, 0, 0, 0.12);
    font-family: "Quicksand", sans-serif;
  }
  .contact {
    position: absolute;
    right: 80px;
    top: 110px;
    margin: 0;
    text-align: right;
    color: var(--azure);
    font-size: 21px;
    font-weight: 500;
    line-height: 33px;
    letter-spacing: 0.2px;
  }
  .rule {
    position: absolute;
    top: 440px;
    height: 2px;
    background: var(--azure);
  }
  .rule--left { left: 0; width: 66px; }
  .rule--right { left: 312px; right: 0; }
  .brand {
    position: absolute;
    left: 78px;
    top: 427px;
    display: flex;
    align-items: center;
    gap: 9px;
    color: var(--azure);
    font-size: 19px;
    font-weight: 600;
    letter-spacing: 1px;
    white-space: nowrap;
  }
  .brand__dot {
    width: 12px;
    height: 12px;
    border-radius: 50%;
    background: var(--azure);
  }
</style>
</head>
<body>
  <section class="card" aria-label="Tidewell Events business card">
    <p class="contact">
      +123 456 789<br>
      email@yourdomain.com<br>
      www.yourdomain.com
    </p>
    <div class="rule rule--left"></div>
    <div class="brand">
      <span class="brand__dot"></span>
      <span class="brand__name">TIDEWELL EVENTS</span>
    </div>
    <div class="rule rule--right"></div>
  </section>
</body>
</html>
```